creation of a business card design for a company specializing in the creation...

I would like to create a design for a professional business card on a black background and with the company's colors (I am attaching some files: including the logo in horizontal and centered format, I am also attaching a recent project design a T-shirt, this is the one I chose to give you an idea of my preferences.

we are in the process of developing a new website design, it is still in the development phase but it can be viewed at the following address: www.vendrelak.be to give you other ideas about the company
you will see for yourself the subject of my main activity: company specializing in the construction of stairs

I would like a business card that stands out from the rest with a unique design

here is the informations
Name: Florent Dubrec
Function: Manager
Address: Rue Masquelin du Pont 41
7180 La Louvière
telephone: +32 486 219 508
email: info@rv8k.be
website: rv8k. be
social networks: Facebook, YouTube, TikTok, Instagram

Target Market(s)

customer who wants to have a beautiful staircase built

Industry/Entity Type

contruction d'escalier

Contact Information for Business Card

Adresse. Numero de telephone, site web, le texte : "Createur d'escalier", logo recto-verso, icone des reseaux sociaux

Requirements
Must have
• the mention: Stair creator
Nice to have
• an illustration of a designer staircase
Should not have
• do not distort the logo

```html
<!DOCTYPE html>
<html lang="en">
<head>
<meta charset="utf-8">
<title>RV8K business card</title>
<link rel="stylesheet" href="https://fonts.googleapis.com/css2?family=Montserrat:wght@400;500;700;800&display=swap">
<style>
  :root {
    --stage: #2b2b2b;
    --card: #1a1a1b;
    --white: #ffffff;
    --blue: #6798b8;
    --blue-light: #9fbfd4;
    --blue-dark: #3b6d8e;
  }
  * { box-sizing: border-box; margin: 0; padding: 0; }
  html, body {
    width: 1200px; height: 900px; overflow: hidden;
    background: var(--stage);
    font-family: "Montserrat", sans-serif;
  }
  .stage {
    width: 1200px; height: 900px;
    display: flex; flex-direction: column; align-items: center; justify-content: center;
    gap: 40px;
  }
  .card {
    position: relative;
    width: 700px; height: 400px;
    background: var(--card);
    overflow: hidden;
    box-shadow: 0 10px 30px rgba(0,0,0,.45);
  }

  /* Brand block */
  .brand { display: flex; align-items: center; gap: 18px; }
  .brand-mark { width: 48px; height: 48px; background: var(--blue); flex: none; }
  .brand-name {
    font-weight: 500; color: var(--white);
    font-size: 100px; letter-spacing: 10px; line-height: 1;
  }
  .tagline {
    color: var(--blue); font-weight: 500;
    font-size: 15px; letter-spacing: 9px; text-transform: uppercase;
    line-height: 1; white-space: nowrap;
  }

  /* Back side */
  .card-back {
    display: flex; flex-direction: column; align-items: center; justify-content: center;
  }
  .card-back .tagline { margin-top: 14px; }
  .follow { display: flex; align-items: center; gap: 12px; margin-top: 34px; }
  .follow-label { color: var(--blue); font-weight: 700; font-size: 32px; }
  .social { width: 26px; height: 26px; border-radius: 50%; background: var(--blue); }

  /* Front side */
  .card-front .brand-block { position: absolute; left: 58px; top: 40px; }
  .card-front .brand { gap: 12px; }
  .card-front .brand-mark { width: 24px; height: 24px; }
  .card-front .brand-name { font-size: 50px; letter-spacing: 5px; }
  .card-front .tagline { font-size: 8px; letter-spacing: 5px; margin-top: 8px; }

  .identity { position: absolute; left: 44px; top: 150px; padding-left: 22px; }
  .identity::before {
    content: ""; position: absolute; left: 0; top: 4px;
    width: 12px; height: 54px; background: var(--blue);
  }
  .person { color: var(--blue); font-weight: 800; font-size: 30px; line-height: 1.1; }
  .role { color: var(--white); font-size: 20px; font-weight: 400; }

  .contacts { position: absolute; left: 66px; top: 232px; list-style: none; }
  .contacts li {
    display: flex; align-items: center; gap: 10px;
    color: var(--white); font-size: 19px; line-height: 28px;
  }
  .contacts svg { width: 16px; height: 16px; fill: var(--blue); flex: none; }

  .address {
    position: absolute; left: 50px; top: 326px;
    color: var(--white); font-size: 19px; line-height: 26px; font-style: normal;
  }

  .decoration {
    position: absolute; right: 0; top: 40px;
    width: 330px; height: 330px;
    background: linear-gradient(135deg, var(--blue-light) 0%, var(--blue) 60%, var(--blue-dark) 100%);
  }
</style>
</head>
<body>
<main class="stage">
  <section class="card card-back">
    <div class="brand">
      <span class="brand-mark"></span>
      <span class="brand-name">RV8K</span>
    </div>
    <p class="tagline">Original Staircases</p>
    <div class="follow">
      <span class="follow-label">Follow Us</span>
      <span class="social"></span>
      <span class="social"></span>
      <span class="social"></span>
      <span class="social"></span>
    </div>
  </section>

  <section class="card card-front">
    <div class="brand-block">
      <div class="brand">
        <span class="brand-mark"></span>
        <span class="brand-name">RV8K</span>
      </div>
      <p class="tagline">Original Staircases</p>
    </div>

    <div class="identity">
      <p class="person">Florent Dubrec</p>
      <p class="role">Function Manager</p>
    </div>

    <ul class="contacts">
      <li>
        <svg viewBox="0 0 16 16"><path d="M3 1h3l1 4-2 1a9 9 0 0 0 5 5l1-2 4 1v3c0 1-1 2-2 2A13 13 0 0 1 1 3c0-1 1-2 2-2z"/></svg>
        +32 486 219 508
      </li>
      <li>
        <svg viewBox="0 0 16 16"><path d="M1 3h14v10H1z M1 3l7 6 7-6" stroke="#1a1a1b" stroke-width="1.2"/></svg>
        info@rv8k.be
      </li>
      <li>
        <svg viewBox="0 0 16 16"><circle cx="8" cy="8" r="7"/><path d="M1 8h14M8 1c3 3 3 11 0 14M8 1c-3 3-3 11 0 14" stroke="#1a1a1b" fill="none" stroke-width="1"/></svg>
        www.rv8k. be
      </li>
    </ul>

    <address class="address">
      Rue Masquelin du Pont 41<br>
      7180 La Louvière
    </address>

    <div class="decoration" role="img" aria-label="Large staircase brand decoration in light and mid blue"></div>
  </section>
</main>
</body>
</html>
```